Brightfield Optics seeks updated contemporary business card

Brightfield Optics utilizes advanced technology and we take pride in the modern look and feel of our practice. We like our current card, but it's been four years so it is time for an update.

Target Market(s)

Females 25-45 make the most health care decisions for their family.

Contact Information for Business Card

Clean front. Back with info and with empty space for appointment time or other small note

Requirements
Must have
• Logo
Ridge Marketvale, 28413 E Larkspur Ave
Cedar Terrace Marketvale, 4638 S Dunmore Rd
Call or text: 509-342-1968
email: hello@brightfieldoptics.example
brightfieldoptics.example
Dr Tobias Werring & Associates

```html
<!DOCTYPE html>
<html lang="en">
<head>
<meta charset="utf-8">
<title>Brightfield Optics – Business Card</title>
<link rel="stylesheet" href="https://fonts.googleapis.com/css2?family=Open+Sans:ital,wght@0,400;0,600;0,700;1,400&family=Exo+2:wght@600&display=swap">
<style>
  :root {
    --backdrop: #dcdde1;
    --card: #f4f4f5;
    --ink: #2b2b2b;
    --navy: #1f3f6a;
    --blue: #1a8fc8;
    --band-start: #15557f;
    --band-end: #1b7db2;
    --rule: #ffffff;
  }
  * { box-sizing: border-box; margin: 0; padding: 0; }
  html, body { width: 1200px; height: 1200px; overflow: hidden; }
  body { background: var(--backdrop); font-family: "Open Sans", Arial, sans-serif; color: var(--ink); position: relative; }

  .card {
    position: absolute; left: 290px; width: 630px; height: 359px;
    background: linear-gradient(135deg, #f7f7f8 0%, #ededee 100%);
    overflow: hidden;
  }
  .card--front { top: 196px; }
  .card--back { top: 645px; background: linear-gradient(180deg, #fafafa 0%, #f1f1f2 60%, #e9e9ea 100%); }

  .brand { position: absolute; display: flex; align-items: center; gap: 8px; }
  .brand__dot { width: 14px; height: 14px; border-radius: 50%; background: var(--blue); }
  .brand__name { font-weight: 700; font-size: 21px; color: var(--navy); letter-spacing: .2px; }

  /* front */
  .face-photo {
    position: absolute; left: 238px; top: 0; width: 392px; height: 359px;
    background: linear-gradient(90deg, rgba(225,225,227,0) 0%, #dcdcde 45%, #cfcfd2 100%);
  }
  .eye-photo {
    position: absolute; left: 373px; top: 16px; width: 239px; height: 186px;
    border-radius: 12px;
    background: radial-gradient(ellipse at 50% 50%, #7fa6d6 0%, #b9c3cf 22%, #e1e1e3 55%, #d3d3d5 100%);
    box-shadow: 0 0 10px rgba(255,255,255,.9);
  }
  .guide { position: absolute; background: var(--rule); }
  .guide--h { left: 226px; top: 105px; width: 150px; height: 2px; }
  .guide--v { left: 423px; top: 202px; width: 2px; height: 157px; }

  .contact { position: absolute; left: 50px; top: 176px; list-style: none; font-size: 15px; line-height: 18px; }
  .contact li { display: flex; align-items: center; gap: 8px; }
  .contact svg { width: 12px; height: 12px; fill: var(--blue); flex: none; }
  .contact .note { color: var(--blue); }

  .address { position: absolute; left: 50px; top: 249px; font-size: 15px; line-height: 18px; font-style: normal; }

  .practice { position: absolute; right: 50px; top: 301px; font-weight: 600; font-size: 16px; color: var(--blue); }
  .practice::before { content: ""; position: absolute; right: 0; top: -15px; width: 31px; height: 3px; background: var(--blue); }

  /* back */
  .appt-title { position: absolute; right: 46px; top: 66px; font-family: "Exo 2", "Open Sans", sans-serif; font-weight: 600; font-size: 24px; color: var(--blue); }
  .appt-title span { color: var(--navy); }

  .field-row { position: absolute; left: 62px; width: 504px; display: flex; align-items: baseline; font-size: 15px; }
  .field-row--name { top: 163px; }
  .field-row--date { top: 203px; }
  .field-line { flex: 1; border-bottom: 1.5px dotted #555; margin: 0 2px; transform: translateY(-3px); }
  .field-line--date { flex: 0 0 238px; }
  .field-line--time { flex: 0 0 130px; }
  .field-gap { width: 4px; }

  .day { position: absolute; top: 244px; display: flex; align-items: center; gap: 5px; font-size: 15px; }
  .day__box { width: 30px; height: 17px; border: 1.5px solid var(--blue); border-radius: 2px; }

  .policy-band {
    position: absolute; left: 0; top: 310px; width: 630px; height: 32px;
    background: linear-gradient(90deg, var(--band-start), var(--band-end));
    color: #fff; font-style: italic; font-size: 14.5px;
    display: flex; align-items: center; justify-content: center;
  }
</style>
</head>
<body>
  <section class="card card--front">
    <div class="face-photo" role="img" aria-label="Soft greyscale photograph of a woman's face"></div>
    <div class="eye-photo" role="img" aria-label="Framed close-up photograph of a blue eye"></div>
    <div class="guide guide--h"></div>
    <div class="guide guide--v"></div>

    <div class="brand" style="left:50px; top:86px;">
      <span class="brand__dot"></span>
      <span class="brand__name">Brightfield Optics</span>
    </div>

    <ul class="contact">
      <li><svg viewBox="0 0 24 24"><path d="M6.6 10.8a15.1 15.1 0 0 0 6.6 6.6l2.2-2.2c.3-.3.7-.4 1-.2 1.1.4 2.3.6 3.6.6.6 0 1 .4 1 1V20c0 .6-.4 1-1 1A17 17 0 0 1 3 4c0-.6.4-1 1-1h3.5c.6 0 1 .4 1 1 0 1.3.2 2.5.6 3.6.1.3 0 .7-.2 1z"/></svg><span>509-342-1968 <span class="note">(Call / SMS)</span></span></li>
      <li><svg viewBox="0 0 24 24"><path d="M2 5h20v14H2z M2 5l10 8 10-8" fill="none" stroke="#1a8fc8" stroke-width="2.5"/></svg><span>hello@brightfieldoptics.example</span></li>
      <li><svg viewBox="0 0 24 24"><circle cx="12" cy="12" r="9.5" fill="none" stroke="#1a8fc8" stroke-width="2"/><path d="M2.5 12h19M12 2.5c-5 5-5 14 0 19M12 2.5c5 5 5 14 0 19" fill="none" stroke="#1a8fc8" stroke-width="1.6"/></svg><span>www.brightfieldoptics.example</span></li>
    </ul>

    <address class="address">
      Ridge Marketvale<br>
      28413 E Larkspur Ave<br>
      Cedar Terrace Marketvale<br>
      4638 S Dunmore Rd
    </address>

    <div class="practice">Dr Tobias Werring &amp; Associates</div>
  </section>

  <section class="card card--back">
    <div class="brand" style="left:62px; top:86px;">
      <span class="brand__dot"></span>
      <span class="brand__name">Brightfield Optics</span>
    </div>

    <h2 class="appt-title"><span>Next</span> Appointment</h2>

    <div class="field-row field-row--name">Name:<span class="field-line"></span></div>
    <div class="field-row field-row--date">Date:<span class="field-line field-line--date"></span><span class="field-gap"></span>Time:<span class="field-line field-line--time"></span><span class="field-gap"></span>am/pm</div>

    <div class="day" style="left:62px;">Mon. <span class="day__box"></span></div>
    <div class="day" style="left:179px;">Tue. <span class="day__box"></span></div>
    <div class="day" style="left:287px;">Wed. <span class="day__box"></span></div>
    <div class="day" style="left:404px;">Thu. <span class="day__box"></span></div>
    <div class="day" style="left:509px;">Fri. <span class="day__box"></span></div>

    <div class="policy-band">If you are unable to keep your appointment please call the office 24 hours in advance.</div>
  </section>
</body>
</html>
```